Salon and Spa Distributor Business Card

Need a business card. We are are distributor in the salon and spa industry. We identify with natural beauty. Need a card with:
Company Name: Petal Haven"
Title: "President & CEO"
Address
Company Phone number
email
website
Tag Line:" Naturally Sourced Salon Supply"

Industry/Entity Type

Business

Contact Information for Business Card

Name: Lena Morcott
Title: "President & CEO"
Address: 317 Birchfield Ln, Oakvane, NJ 07481
Company Phone number: 800-463-9152
email: lenamorcott@petalhaven-example.com
website: www.petalhaven-example.com

Requirements
Should not have
• No black backgrounds

```html
<!DOCTYPE html>
<html lang="en">
<head>
<meta charset="utf-8">
<title>Petal Haven – Business Card</title>
<link rel="stylesheet" href="https://fonts.googleapis.com/css2?family=Cormorant+Garamond:ital,wght@0,500;0,700;1,500&family=Sorts+Mill+Goudy:ital@0;1&display=swap">
<style>
  :root {
    --brand-blue: #2c4a9e;
    --ink: #2a2a2a;
    --paper: #ffffff;
    --sky: #5aa6dc;
    --cloud: #e8f2fa;
    --foliage: #5f9a2e;
    --foliage-deep: #3f7321;
    --water: #1f8fb4;
    --water-deep: #0f6a8c;
  }
  * { margin: 0; padding: 0; box-sizing: border-box; }
  html, body {
    width: 1200px; height: 686px; overflow: hidden;
    background: var(--paper);
  }
  .card {
    position: relative;
    width: 1200px; height: 686px;
    background: var(--paper);
    overflow: hidden;
    font-family: "Sorts Mill Goudy", "Cormorant Garamond", serif;
  }
  .scenery {
    position: absolute;
    left: 594px; top: 0;
    width: 606px; height: 686px;
    background:
      linear-gradient(180deg,
        var(--sky) 0%,
        var(--cloud) 22%,
        #d9ebc4 34%,
        var(--foliage) 48%,
        var(--foliage-deep) 66%,
        var(--water) 78%,
        var(--water-deep) 100%);
    -webkit-mask-image: linear-gradient(90deg, transparent 0%, rgba(0,0,0,.6) 16%, #000 32%);
            mask-image: linear-gradient(90deg, transparent 0%, rgba(0,0,0,.6) 16%, #000 32%);
  }
  .details { position: absolute; left: 42px; top: 0; }
  .line { position: absolute; left: 0; white-space: nowrap; line-height: 1; font-weight: 400; }
  .company-name {
    top: 46px; font-size: 80px; color: var(--brand-blue);
    letter-spacing: 0.5px;
  }
  .tagline {
    top: 144px; font-size: 38px; font-style: italic; color: var(--ink);
  }
  .person-name {
    top: 233px; font-size: 74px; color: var(--brand-blue);
  }
  .job-title {
    top: 314px; font-size: 40px; color: var(--ink);
  }
  .address, .phone {
    font-family: "Cormorant Garamond", serif; font-weight: 700;
    font-size: 46px; color: var(--brand-blue);
    font-variant-numeric: lining-nums;
  }
  .address-street { top: 394px; }
  .address-city { top: 448px; }
  .phone { top: 508px; }
  .email, .website {
    font-size: 33px; color: var(--ink);
  }
  .email { top: 571px; }
  .website { top: 613px; }
</style>
</head>
<body>
  <main class="card">
    <div class="scenery" role="img" aria-label="Photo of a waterfall cascading into a turquoise lake beneath lush green trees and a blue, cloudy sky"></div>
    <section class="details">
      <h1 class="line company-name">Petal Haven</h1>
      <p class="line tagline">“Naturally Sourced Salon Supply”</p>
      <h2 class="line person-name">Lena Morcott</h2>
      <p class="line job-title">President &amp; CEO</p>
      <p class="line address address-street">317 Birchfield Ln</p>
      <p class="line address address-city">Oakvane, NJ 07481</p>
      <p class="line phone">800-463-9152</p>
      <p class="line email">lenamorcott@petalhaven-example.com</p>
      <p class="line website">www.petalhaven-example.com</p>
    </section>
  </main>
</body>
</html>
```